QEV Blaze Global Packaging for Retail sales sachets and boxes

Firstly what is QEV Blaze - QEV Blaze is a powerful combustion and cleaning technology, developed to help enhance engine performance and responsiveness. Its unique double action formulation is designed to actively clean your engine and protect vital engine parts to help deliver more powerful performance. http://qevtechnics.com.au/
We are branching out into retail sales and require dynamic and innovative packaging to suit an international market place in western and eastern markets.
The core image is the Singapore Lion and the flame, enhancing the visual impact of the flame inline with the QEV colour scheme is desired. QEV Blaze is the product name. For the boxes key info Patented Nitroparaffins, Improved Detergency & Combustion *U.S.EPA Registered* / *U.S. Patents*, Directions for Use: Fill fuel tank, tear sachet, pour contents of sachet into fuel tank, ideal mix ratio is 1ml QEV to every 1L of fuel, (diesel or petrol - depending on the targeted market), Circular flammable symbol with a line through the struck match, FLAMMABLE, Keep away from heat, sparks, and open flame. DO NOT puncture packageing, each box contains X sachets of X mls each, Distributed by: Distributed by: QEV Technics Australia, 47 Tembusu Lane, Singapore 077412, Packaged by: Rivora-Seal Works Sdn Bhd (736492-K) 7C Wisma Kelara Hadi, 9 Jalan Tepian, 10000 Penang, Malaysia Tel/Fax: +604-517 2946 Email: rsw@rivoraseal.net.my Website: http://www.rivoraseal.net.my., MSDS available on website
Sachets: There are two products QEV100 for petrol engines and QEV200 for diesel engines.
Info for sachets: QEV Blaze, the Lion image as per above, QEV100 (this will be either QEV100 or QEV 200), Additive for Petrol Engine (or diesel engines depending on content of sachet), Directions for Use, Fill fuel tank, tear sachet, pour contents of sachet into fuel tank, ideal mix ratio is 1ml QEV to every 1L of fuel, Net Content Xml, QEV is a patented fuel technology that uses a nitro paraffin concentrate, blended with fuels to improve their atomization, lubricity and combustion quality to achieve more green mileage (we will consider changing this wording if a better description is presented), Circular flammable symbol with a line through the struck match, FLAMMABLE, Keep away from heat, sparks, and open flame. DO NOT puncture packageing, Distributed by: QEV Technics Australia, 47 Tembusu Lane, Singapore 077412, info@qevtechnics.com.au. MSDS available on website, Please refer to the attached packaging size specifications, refer to the webpage etc to ensure uniformity of branding.
Updates

To all the designers thank you for your interest. After viewing some of the first submission I need to clarify that the images of the packaging sachets and boxes is just info please refer to the design brief for the required content. Look forward to your submissions

Project Deadline Extended
Reason: Finalist designs set to board for comment and additional time required to finalise the amendments required.

Industry/Entity Type

Retail

```html
<!DOCTYPE html>
<html lang="en">
<head>
<meta charset="utf-8">
<title>QEV200 Sachet – Additive for Petrol Engine</title>
<link href="https://fonts.googleapis.com/css2?family=Montserrat:wght@600;700;800&family=Open+Sans:wght@400;700&family=Racing+Sans+One&display=swap" rel="stylesheet">
<style>
  :root {
    --stage: #d4d4d4;
    --cyan: #19bfe2;
    --navy: #2a3f95;
    --navy-dark: #1e2f7a;
    --white: #ffffff;
    --copy-soft: #c4ecf7;
  }
  * { box-sizing: border-box; margin: 0; padding: 0; }
  html, body { width: 762px; height: 1200px; overflow: hidden; }
  body {
    background: var(--stage);
    font-family: "Open Sans", Arial, sans-serif;
    position: relative;
  }
  .sachet {
    position: absolute;
    left: 165px; top: 35px;
    width: 447px; height: 1125px;
    overflow: hidden;
    background: var(--cyan);
  }
  .sachet-art { position: absolute; inset: 0; }
  .brand {
    position: absolute;
    left: 80px; top: 150px;
    display: flex; align-items: center; gap: 14px;
  }
  .brand-dot {
    width: 48px; height: 48px; border-radius: 50%;
    background: var(--navy);
  }
  .brand-name {
    font-family: "Montserrat", Arial, sans-serif;
    font-weight: 700;
    font-size: 30px;
    line-height: 1;
    color: var(--navy);
  }
  .product-ribbon {
    position: absolute; left: 40px; top: 452px;
    width: 370px; height: 110px;
  }
  .product-code {
    position: absolute; left: 0; right: 0; top: 487px;
    text-align: center;
    font-family: "Montserrat", Arial, sans-serif;
    font-weight: 800;
    font-size: 40px;
    letter-spacing: 1px;
    color: var(--white);
    line-height: 1;
  }
  .product-type {
    position: absolute; left: 0; right: 0; top: 538px;
    text-align: center;
    font-family: "Montserrat", Arial, sans-serif;
    font-weight: 700;
    font-size: 14.5px;
    color: var(--white);
  }
  .tagline {
    position: absolute; left: 0; right: 0; top: 632px;
    text-align: center;
    font-family: "Racing Sans One", Impact, sans-serif;
    font-style: italic;
    font-size: 30px;
    line-height: 44px;
    letter-spacing: 5px;
    color: var(--white);
    text-transform: uppercase;
  }
  .directions {
    position: absolute; left: 88px; right: 88px; top: 866px;
    text-align: center;
  }
  .directions-title {
    font-weight: 700; font-size: 14.5px; color: var(--white);
    margin-bottom: 14px;
  }
  .directions-copy {
    font-size: 14.5px; line-height: 21px; color: var(--copy-soft);
  }
  .net-content {
    position: absolute; left: 0; right: 0; top: 1038px;
    text-align: center;
    font-weight: 700; font-size: 14px; color: var(--white);
  }
</style>
</head>
<body>
  <main class="sachet">
    <svg class="sachet-art" width="447" height="1125" viewBox="0 0 447 1125" aria-hidden="true">
      <defs>
        <linearGradient id="top-field" x1="0" y1="0" x2="0.3" y2="1">
          <stop offset="0" stop-color="#c8f1fb"/>
          <stop offset="0.45" stop-color="#7fdcf4"/>
          <stop offset="1" stop-color="#3cc6ea"/>
        </linearGradient>
        <linearGradient id="deep-sweep" x1="0" y1="0" x2="0" y2="1">
          <stop offset="0" stop-color="#0a6d8d"/>
          <stop offset="1" stop-color="#0f92b4"/>
        </linearGradient>
        <linearGradient id="lower-field" x1="0" y1="0" x2="0" y2="1">
          <stop offset="0" stop-color="#0f9cc0"/>
          <stop offset="0.5" stop-color="#16b4da"/>
          <stop offset="1" stop-color="#0da6cc"/>
        </linearGradient>
      </defs>
      <rect width="447" height="1125" fill="url(#lower-field)"/>
      <rect width="447" height="520" fill="url(#top-field)"/>
      <path d="M0 430 Q180 280 447 232 L447 640 Q220 600 0 760 Z" fill="url(#deep-sweep)"/>
      <path d="M0 470 Q200 340 447 300 L447 360 Q230 390 0 560 Z" fill="#0c84a6" opacity="0.55"/>
      <path d="M0 760 Q220 600 447 640 L447 1125 L0 1125 Z" fill="url(#lower-field)"/>
      <g stroke="#0b86a9" stroke-width="2" opacity="0.7">
        <line x1="0" y1="1068" x2="447" y2="1068"/>
        <line x1="0" y1="1078" x2="447" y2="1078"/>
        <line x1="0" y1="1088" x2="447" y2="1088"/>
      </g>
      <rect x="0" y="1095" width="447" height="30" fill="#0c93b8"/>
    </svg>

    <div class="brand">
      <span class="brand-dot"></span>
      <span class="brand-name">QEV Blaze</span>
    </div>

    <svg class="product-ribbon" viewBox="0 0 370 110" aria-hidden="true">
      <polygon points="2,5 70,5 70,60 28,60 44,32" fill="var(--navy-dark)"/>
      <polygon points="300,30 368,30 352,58 368,88 300,88" fill="var(--navy-dark)"/>
      <polygon points="62,12 310,12 300,72 52,72" fill="var(--navy)"/>
    </svg>
    <div class="product-code">QEV200</div>
    <div class="product-type">ADDITIVE FOR PETROL ENGINE</div>

    <p class="tagline">Specially packed<br>for<br>your motorcycle</p>

    <section class="directions">
      <h2 class="directions-title">Directions for Use</h2>
      <p class="directions-copy">Fill fuel tank, tear sachet, pour contents of sachet into fuel tank, ideal mix ratio is 1ml QEV to every 1L of fuel</p>
    </section>

    <p class="net-content">Net Content 30ml</p>
  </main>
</body>
</html>
```